VORTAL Business Card Design

We need a business card for a new company based on the Gold Coast, we are a new supplement distributing company called VORTAL Sports Nutrition - Bold Horizon Sports Nutrition. We are providing new science based bodybuilding and fitness supplementation. Our company has a key focus towards next generation. We are wanting a card that is cool, innovative and fresh. We would like to see the implementation of the below image in a fresh and very innovative design that stands out. The final design should communicate New, Innovative, Cool, Science and researched based.
Target Market(s)
The target market is fitness and bodybuilder enthusiasts. Young audience so very cool looking.
Industry/Entity Type
Fitness
Contact Information for Business Card
(front of card)
VORTAL Sports Nutrition.
Liam Darrow
CEO/Sport Nutrition Specialist
0472 638 904
Liam@vortalsportsfuel.example
www.vortalsportsfuel.example
(back of card)
Scientifically formulated supplement range
Private Nutrition consultations
comprehensive sports nutrition seminars
Requirements
Nice to have
- The card could have a cut out on one of the sides or one of the corners rounded off so the card looks different from a normal business card.
Should not have
- The colours need to complement each other and pop out.

```html
<!DOCTYPE html>
<html lang="en">
<head>
<meta charset="utf-8">
<title>VORTAL Sports Nutrition – Business Card</title>
<link href="https://fonts.googleapis.com/css2?family=Montserrat:wght@300;400;600;700&display=swap" rel="stylesheet">
<style>
  :root {
    --backdrop: #2b2c2e;
    --card-top: #020304;
    --card-mid: #07131c;
    --card-bottom: #0f2a3b;
    --accent: #5cc4ef;
    --ink: #ffffff;
  }
  * { margin: 0; padding: 0; box-sizing: border-box; }
  html, body {
    width: 1200px; height: 900px; overflow: hidden;
    background: var(--backdrop);
    font-family: "Montserrat", Arial, sans-serif;
  }
  .stage {
    width: 1200px; height: 900px;
    display: flex; align-items: center; justify-content: center; gap: 70px;
  }
  .card {
    width: 340px; height: 580px;
    border-radius: 0 0 0 28px;
    background: radial-gradient(ellipse at 50% 75%, var(--card-bottom) 0%, var(--card-mid) 55%, var(--card-top) 100%);
    box-shadow: 0 18px 40px rgba(0,0,0,0.45);
    color: var(--ink);
    text-align: center;
    display: flex; flex-direction: column; align-items: center;
    text-transform: uppercase;
  }
  .brand-mark {
    display: flex; align-items: center; gap: 10px;
    color: var(--accent); font-weight: 700; letter-spacing: 2px;
  }
  .brand-mark .dot {
    border-radius: 50%; background: var(--accent); display: inline-block;
  }

  /* front */
  .card--front { padding-top: 78px; }
  .card--front .brand-mark { font-size: 40px; }
  .card--front .brand-mark .dot { width: 16px; height: 16px; }
  .company {
    margin-top: 46px; font-size: 22px; font-weight: 700; letter-spacing: 0.3px;
  }
  .company .company__lead { color: var(--ink); }
  .company .company__rest { color: var(--accent); }
  .person { margin-top: 62px; }
  .person__name { color: var(--accent); font-size: 30px; font-weight: 700; }
  .person__role { text-transform: none; font-size: 16px; font-weight: 400; margin-top: 4px; }
  .contact { margin-top: 40px; text-transform: none; }
  .contact__phone { color: var(--accent); font-size: 30px; font-weight: 400; letter-spacing: 1px; }
  .contact__line { font-size: 16px; font-weight: 400; margin-top: 8px; }

  /* back */
  .card--back { padding-top: 110px; }
  .card--back .brand-mark { font-size: 56px; }
  .card--back .brand-mark .dot { width: 22px; height: 22px; }
  .tagline { margin-top: 70px; font-size: 14px; font-weight: 400; letter-spacing: 0.5px; }
  .offer { font-size: 17px; line-height: 1.3; font-weight: 400; }
  .offer--highlight { color: var(--accent); margin-top: 44px; }
  .offer--services { margin-top: 50px; }
</style>
</head>
<body>
<main class="stage">
  <section class="card card--front" aria-label="Business card front">
    <div class="brand-mark"><span class="dot"></span>VORTAL</div>
    <h1 class="company"><span class="company__lead">VORTAL</span> <span class="company__rest">Sports Nutrition</span></h1>
    <div class="person">
      <h2 class="person__name">Liam Darrow</h2>
      <p class="person__role">CEO/Sport Nutrition Specialist</p>
    </div>
    <div class="contact">
      <p class="contact__phone">0472 638 904</p>
      <p class="contact__line">Liam@vortalsportsfuel.example</p>
      <p class="contact__line">www.vortalsportsfuel.example</p>
    </div>
  </section>

  <section class="card card--back" aria-label="Business card back">
    <div class="brand-mark"><span class="dot"></span>VORTAL</div>
    <p class="tagline">Bold Horizon Sports Nutrition</p>
    <p class="offer offer--highlight">Scientifically formulated<br>supplement range</p>
    <p class="offer offer--services">Private nutrition consultations<br>comprehensive sports nutrition<br>seminars</p>
  </section>
</main>
</body>
</html>
```